Recruiting ad for Caregivers and Nurses

We need a few amazing, fun, catchy, creative recruiting ads for Caregivers and Nurses to care for homecare patients on the island of Oahu, in Hawaii. We are an in home care company called Brantley Homecare. Our care services are provided 24/7, so we need staff that can work days, nights, weekdays, weekends. We need catchy fun ads to entice caregivers and nurses to call our office to inquire about jobs available. Our patients age range is from babies to seniors. We need caregivers and nurses for basic patient care (bathing, dressing, ambulating, preparing meals, medication reminders, light housekeeping) and complex patients (oxygen, tube feeding, injections, vents, wound care). Here are some bullets to consider including:
*Full-time and Part-time Positions Available (days, nights, weekdays, weekends)
*Sign-On Bonus Programs Offered up to $500
*Refer a Friend Bonus Program
*Holiday Pay
*2 Health Plans to Choose from
*Island-Wide Locations
*All PPE Provided (masks, gloves, etc)
*401K Program
*Tuition Benefits

```html
<!DOCTYPE html>
<html lang="en">
<head>
<meta charset="utf-8">
<title>Brantley Homecare – Join Our Team</title>
<link href="https://fonts.googleapis.com/css2?family=Cinzel:wght@400;500&family=Source+Sans+3:wght@400;600&display=swap" rel="stylesheet">
<style>
  :root {
    --page-bg: #e9e9e8;
    --paper: #ffffff;
    --blush: #fbe9e4;
    --salmon: #f29a86;
    --teal: #1f6b63;
    --ink: #4a4a4a;
    --rule: #c9c9c9;
    --silver: #cfd1d4;
    --photo-warm: #e9d8b8;
    --photo-light: #f6efe2;
    --photo-blue: #6f8fc8;
  }
  * { margin: 0; padding: 0; box-sizing: border-box; }
  html, body { width: 872px; height: 1200px; overflow: hidden; background: var(--page-bg); }
  .canvas { position: relative; width: 872px; height: 1200px; }

  .ad {
    position: absolute; left: 26px; top: 334px; width: 820px; height: 532px;
    background: linear-gradient(160deg, var(--paper) 30%, var(--blush) 100%);
    overflow: hidden;
    box-shadow: 0 6px 14px rgba(0,0,0,.22);
    font-family: "Source Sans 3", sans-serif;
  }
  .ad-shapes { position: absolute; inset: 0; }

  .headline {
    position: absolute; left: 468px; top: 32px;
    font-family: "Cinzel", serif; font-weight: 400;
    font-size: 36px; letter-spacing: 1px; color: var(--teal); line-height: 1;
    white-space: nowrap;
  }
  .role-bar {
    position: absolute; left: 470px; top: 86px; width: 330px; height: 25px;
    background: var(--salmon);
    color: #fff; font-size: 17px; letter-spacing: 2.4px; text-align: center;
    line-height: 25px; text-transform: uppercase; font-weight: 400;
  }

  .perks { position: absolute; left: 470px; top: 124px; width: 330px; list-style: none; }
  .perk {
    position: relative; padding: 2.5px 0 2.5px 24px;
    font-size: 14.5px; line-height: 15px; color: var(--ink);
    border-bottom: 1px dotted var(--rule);
  }
  .perk:last-child { border-bottom: none; }
  .perk svg { position: absolute; left: 0; top: 3px; width: 14px; height: 14px; }

  .badge-text {
    position: absolute; left: 302px; top: 340px; width: 160px;
    text-align: center; color: #fff; font-family: "Cinzel", serif; line-height: 1.15;
  }
  .badge-text .big { display: block; font-size: 19px; letter-spacing: 2px; }
  .badge-text .small { display: block; font-family: "Source Sans 3", sans-serif; font-size: 12px; letter-spacing: 1.6px; margin-top: 6px; font-weight: 600; }

  .brand {
    position: absolute; right: 22px; top: 392px; width: 170px; text-align: center;
    color: #fff; font-family: "Source Sans 3", sans-serif; font-weight: 600;
    font-size: 23px; line-height: 1.05;
  }
  .brand-mark { display: block; width: 28px; height: 28px; margin: 0 auto 7px; background: #fff; border-radius: 4px; }

  .contact {
    position: absolute; right: 22px; top: 498px;
    display: flex; align-items: center; gap: 10px;
    color: #fff; font-size: 14px; white-space: nowrap;
  }
  .contact-item { display: flex; align-items: center; gap: 5px; }
  .contact-item svg { width: 14px; height: 14px; }
</style>
</head>
<body>
<div class="canvas">
  <section class="ad" aria-label="Brantley Homecare recruiting ad">
    <svg class="ad-shapes" viewBox="0 0 820 532" width="820" height="532">
      <defs>
        <linearGradient id="photoTone" x1="0" y1="0" x2="1" y2="1">
          <stop offset="0" stop-color="var(--photo-light)"/>
          <stop offset="0.45" stop-color="var(--photo-warm)"/>
          <stop offset="0.8" stop-color="var(--photo-blue)"/>
          <stop offset="1" stop-color="#b9c9de"/>
        </linearGradient>
      </defs>

      <path class="photo" role="img" aria-label="Photo: smiling nurse in blue scrubs hugging a happy senior woman outdoors"
            d="M0,0 H376 C470,80 482,300 404,430 C300,455 150,466 0,470 Z" fill="url(#photoTone)"/>

      <path class="accent-arc" d="M386,0 C486,80 494,300 414,430" fill="none" stroke="var(--salmon)" stroke-width="5"/>

      <path class="white-wave" d="M0,466 C250,462 560,362 820,348 L820,532 L0,532 Z" fill="#fff"/>
      <path class="silver-line" d="M0,474 C250,470 560,370 820,356" fill="none" stroke="var(--silver)" stroke-width="4"/>
      <path class="salmon-band" d="M0,488 C250,484 560,386 820,372 L820,532 L0,532 Z" fill="var(--salmon)"/>

      <g class="badge">
        <circle cx="382" cy="392" r="72" fill="var(--teal)"/>
        <circle cx="382" cy="392" r="72" fill="none" stroke="var(--teal)" stroke-width="12"
                stroke-linecap="round" stroke-dasharray="0 18.85"/>
      </g>
    </svg>

    <h1 class="headline">Join our team</h1>
    <div class="role-bar">Caregivers &amp; Nurses</div>

    <ul class="perks">
      <li class="perk"><svg viewBox="0 0 14 14"><circle cx="7" cy="7" r="7" fill="var(--salmon)"/><path d="M4 7.2l2 2 4-4.4" fill="none" stroke="#fff" stroke-width="1.6"/></svg>Full-time and Part-time Positions Available<br>(days, nights, weekdays, weekends)</li>
      <li class="perk"><svg viewBox="0 0 14 14"><circle cx="7" cy="7" r="7" fill="var(--salmon)"/><path d="M4 7.2l2 2 4-4.4" fill="none" stroke="#fff" stroke-width="1.6"/></svg>Sign-On Bonus Programs Offered up to $500</li>
      <li class="perk"><svg viewBox="0 0 14 14"><circle cx="7" cy="7" r="7" fill="var(--salmon)"/><path d="M4 7.2l2 2 4-4.4" fill="none" stroke="#fff" stroke-width="1.6"/></svg>Refer a Friend Bonus Program</li>
      <li class="perk"><svg viewBox="0 0 14 14"><circle cx="7" cy="7" r="7" fill="var(--salmon)"/><path d="M4 7.2l2 2 4-4.4" fill="none" stroke="#fff" stroke-width="1.6"/></svg>Holiday Pay</li>
      <li class="perk"><svg viewBox="0 0 14 14"><circle cx="7" cy="7" r="7" fill="var(--salmon)"/><path d="M4 7.2l2 2 4-4.4" fill="none" stroke="#fff" stroke-width="1.6"/></svg>2 Health Plans to Choose from</li>
      <li class="perk"><svg viewBox="0 0 14 14"><circle cx="7" cy="7" r="7" fill="var(--salmon)"/><path d="M4 7.2l2 2 4-4.4" fill="none" stroke="#fff" stroke-width="1.6"/></svg>Island-Wide Locations</li>
      <li class="perk"><svg viewBox="0 0 14 14"><circle cx="7" cy="7" r="7" fill="var(--salmon)"/><path d="M4 7.2l2 2 4-4.4" fill="none" stroke="#fff" stroke-width="1.6"/></svg>All PPE Provided (masks, gloves, etc)</li>
      <li class="perk"><svg viewBox="0 0 14 14"><circle cx="7" cy="7" r="7" fill="var(--salmon)"/><path d="M4 7.2l2 2 4-4.4" fill="none" stroke="#fff" stroke-width="1.6"/></svg>401K Program</li>
      <li class="perk"><svg viewBox="0 0 14 14"><circle cx="7" cy="7" r="7" fill="var(--salmon)"/><path d="M4 7.2l2 2 4-4.4" fill="none" stroke="#fff" stroke-width="1.6"/></svg>Tuition Benefits</li>
    </ul>

    <p class="badge-text">
      <span class="big">We’re</span>
      <span class="big">Recruiting</span>
      <span class="small">APPLY NOW</span>
    </p>

    <div class="brand"><span class="brand-mark"></span>Brantley Homecare</div>

    <div class="contact">
      <span class="contact-item">Inquire within</span>
      <span class="contact-item">
        <svg viewBox="0 0 14 14"><circle cx="7" cy="7" r="7" fill="#fff"/><path d="M4.6 3.6l1.4 1.6-.7 1a5 5 0 0 0 2.5 2.5l1-.7 1.6 1.4-.9 1.1C6.8 10.4 3.6 7.2 3.5 4.5z" fill="var(--salmon)"/></svg>
        808-555-0142
      </span>
      <span class="contact-item">
        <svg viewBox="0 0 14 14"><circle cx="7" cy="7" r="6.3" fill="none" stroke="#fff" stroke-width="1.4"/><ellipse cx="7" cy="7" rx="2.6" ry="6.3" fill="none" stroke="#fff" stroke-width="1.1"/><path d="M1 7h12" stroke="#fff" stroke-width="1.1"/></svg>
        www.brantleycare.com
      </span>
    </div>
  </section>
</div>
</body>
</html>
```